Financial Advisor / Asset Manager Zup Design

I'm currently hosting with Zup and my first attempt at a website is live at www.ravenholtwealth.example Clearly I am not a web designer and I need help making this more catchy, modern, cross-platform compatible, search engine optimized, etc. I've got logos, hex color pallets, and a slew of other graphics. I'm interested in working with a winning designer to write/refine my copy/language to complete the build.

Full set of graphics https://pics.lumora-share.example/q71TzR05KwPd2MhXN do NOT use the CONSULTING graphics as this is for a related business / different website

Target Market(s)

Individuals, small institutions, endowments, non-profits seeking financial advice and asset / portfolio management

Industry/Entity Type

Financial Services

Coding

Coded - Design and coding required

Font styles to use
Other font styles liked:
• AvenirLTStd - Black, Book, and Roman as appropriate

Requirements
Must have
• Complete, cross platform website integrating my existing logo
Nice to have
• Easy to update format for go-forward maintenance

```html
<!DOCTYPE html>
<html lang="en">
<head>
<meta charset="utf-8">
<title>Ravenholt Wealth</title>
<link rel="stylesheet" href="https://fonts.googleapis.com/css2?family=Mulish:wght@400;500;600;700;800;900&display=swap">
<style>
:root{
  --blue:#1b7ccc;
  --blue-deep:#0f5fa8;
  --blue-soft:#d9e9f7;
  --navy:#1c2735;
  --text:#3c4652;
  --muted:#6b7682;
  --white:#ffffff;
  --black:#050608;
  --line:#9cc4e6;
}
*{margin:0;padding:0;box-sizing:border-box}
html,body{width:1200px;height:4594px;overflow:hidden;background:var(--white)}
body{position:relative;font-family:"Mulish",sans-serif;color:var(--text)}
.abs{position:absolute}
.btn{position:absolute;border:2px solid var(--blue);color:var(--blue);font-weight:800;font-size:14px;letter-spacing:.5px;display:flex;align-items:center;justify-content:center;background:var(--white)}

/* hero */
.hero{left:0;top:0;width:1200px;height:850px;overflow:hidden}
.hero-photo{position:absolute;inset:0;
  background:
    radial-gradient(ellipse 260px 330px at 40px 470px,rgba(20,38,24,.95),rgba(20,38,24,0) 100%),
    radial-gradient(ellipse 300px 300px at 1150px 430px,rgba(38,58,22,.95),rgba(38,58,22,0) 100%),
    radial-gradient(ellipse 230px 170px at 390px 520px,rgba(235,238,240,.9),rgba(235,238,240,0) 100%),
    radial-gradient(ellipse 230px 190px at 800px 500px,rgba(235,238,240,.9),rgba(235,238,240,0) 100%),
    linear-gradient(180deg,#1b7ccc 0%,#2b87d2 24%,#9fbfd9 30%,#e3ecf2 37%,#8aa4ba 45%,#4b6b86 52%,#2f4d3a 60%,#3d5a4a 66%,#5d7f9c 74%,#2b5a8a 86%,#17426e 100%)}
.nav{position:absolute;top:66px;left:0;width:1200px;height:36px;color:var(--white);font-size:13.5px;font-weight:700}
.nav a{position:absolute;top:10px;color:var(--white);text-decoration:none}
.nav .active{border-bottom:2px solid var(--white);padding-bottom:16px}
.brand{position:absolute;left:510px;top:16px;width:180px;text-align:center;color:var(--white);font-weight:500;font-size:25px;letter-spacing:1px;line-height:1}
.brand small{display:block;font-size:12px;letter-spacing:3px;margin-top:5px}
.phone-pill{position:absolute;left:944px;top:0;width:166px;height:40px;border:2px solid var(--white);border-radius:20px;display:flex;align-items:center;justify-content:center;gap:6px;font-size:13.5px}
.hero-title{position:absolute;top:176px;width:440px;text-align:center;color:var(--white);font-size:29px;line-height:35px;font-weight:800}
.hero-title span{font-weight:400}

/* who */
.who h2{position:absolute;top:892px;width:420px;text-align:center;color:var(--blue);font-size:28px;font-weight:800}
.who p{position:absolute;top:942px;text-align:center;font-size:16px;line-height:29px;color:var(--text)}
.who .divider{position:absolute;left:600px;top:892px;width:1px;height:178px;background:var(--line)}
.illus{position:absolute;background:radial-gradient(ellipse at 50% 50%,rgba(27,124,204,.26) 0%,rgba(27,124,204,.12) 40%,rgba(27,124,204,.04) 62%,rgba(255,255,255,0) 75%)}

/* why */
.why{left:0;top:1441px;width:1200px;height:716px;background:
  radial-gradient(ellipse 700px 180px at 600px 660px,#e6ebf0,rgba(230,235,240,0)),
  linear-gradient(180deg,#f6f9fc 0%,#eef2f6 55%,#d9e0e7 100%)}
.eyebrow{position:absolute;width:1200px;text-align:center;font-size:14px;letter-spacing:2px;color:var(--muted)}
.section-title{position:absolute;width:1200px;text-align:center;font-size:34px;font-weight:800;color:var(--blue)}
.card{position:absolute;width:342px;height:110px;border:1.5px solid var(--line);border-radius:55px;background:rgba(255,255,255,.55)}
.card .icon{position:absolute;top:7px;width:96px;height:96px;border-radius:50%;border:3px solid var(--blue);background:var(--white);display:flex;align-items:center;justify-content:center}
.card h3{position:absolute;top:28px;font-size:17px;font-weight:800;color:var(--navy)}
.card p{position:absolute;top:55px;font-size:12.5px;line-height:20px;color:var(--muted)}
.card.l .icon{right:7px}.card.l h3,.card.l p{right:118px;text-align:right;width:200px}
.card.r .icon{left:7px}.card.r h3,.card.r p{left:118px;width:210px}
.hub{position:absolute;left:463px;top:192px;width:286px;height:286px;border-radius:50%;border:2px solid var(--line)}
.hub-img{position:absolute;left:20px;top:20px;width:242px;height:242px;border-radius:50%;background:
  linear-gradient(180deg,rgba(255,255,255,0) 45%,rgba(10,70,130,.35) 70%,rgba(27,124,204,.2) 100%),
  radial-gradient(circle at 50% 35%,#5aaaea,#1b7ccc 60%,#115a9c)}

/* services */
.timeline{left:593px;top:2323px;width:2px;height:994px;background:var(--line)}
.dot{position:absolute;left:587px;width:14px;height:14px;border-radius:50%;border:3px solid var(--blue);background:var(--white)}
.svc h3{position:absolute;width:420px;text-align:center;font-size:24px;font-weight:700;color:var(--navy)}
.svc p{position:absolute;width:420px;text-align:center;font-size:15px;line-height:24px;color:var(--text)}

/* contact */
.contact{left:0;top:3625px;width:1200px;height:560px;background:
  radial-gradient(ellipse 500px 220px at 1050px 90px,rgba(255,255,255,.12),rgba(255,255,255,0)),
  radial-gradient(ellipse 500px 200px at 150px 120px,rgba(255,255,255,.1),rgba(255,255,255,0)),
  linear-gradient(180deg,#1b7ccc,#1466b2)}
.contact .label{position:absolute;left:135px;top:96px;color:var(--white);font-size:14px}
.contact h2{position:absolute;left:135px;top:114px;color:var(--white);font-size:33px;font-weight:700}
.info{position:absolute;left:140px;color:var(--white);font-size:16px;line-height:27px;display:flex;gap:14px;align-items:center}
.form{position:absolute;left:536px;top:89px;width:552px;height:374px;background:var(--white);border-radius:0 110px 0 110px}
.field{position:absolute;height:38px;border:1.5px solid #b7c3cf;border-radius:19px;font-size:13px;color:#8a949e;padding:10px 0 0 22px}
.send{position:absolute;left:39px;top:293px;width:172px;height:46px;border-radius:23px;background:var(--blue);color:var(--white);font-size:13px;font-weight:800;letter-spacing:.5px;display:flex;align-items:center;justify-content:center}

/* footer */
.footer{left:0;top:4172px;width:1200px;height:422px;background:var(--black);color:var(--white)}
.footer .col{position:absolute;top:120px}
.footer h4{font-size:14px;font-weight:800;margin-bottom:14px}
.footer li{list-style:none;font-size:13.5px;line-height:26px}
.footer .vbar{position:absolute;top:118px;width:2px;height:20px;background:var(--white)}
.copyright{position:absolute;top:386px;width:1200px;text-align:center;font-size:12.5px;color:#a9b0b7}
.foot-rule{position:absolute;left:0;top:358px;width:1200px;height:1px;background:#24282d}
</style>
</head>
<body>

<section class="abs hero">
  <div class="hero-photo" role="img" aria-label="Mountain lake landscape with paper bear and bull sculptures made of stock pages"></div>
  <nav class="nav">
    <a href="#" class="active" style="left:158px">HOME</a>
    <a href="#" style="left:268px">ABOUT US</a>
    <a href="#" style="left:400px">SERVICES</a>
    <div class="brand">RAVENHOLT<small>WEALTH</small></div>
    <a href="#" style="left:728px">FAQS</a>
    <a href="#" style="left:828px">CONTACT US</a>
    <div class="phone-pill">
      <svg width="13" height="13" viewBox="0 0 24 24"><path fill="#fff" d="M6.6 10.8a15 15 0 0 0 6.6 6.6l2.2-2.2c.3-.3.7-.4 1-.2 1.1.4 2.3.6 3.6.6.6 0 1 .4 1 1V20c0 .6-.4 1-1 1A17 17 0 0 1 3 4c0-.6.4-1 1-1h3.5c.6 0 1 .4 1 1 0 1.3.2 2.5.6 3.6.1.3 0 .7-.2 1z"/></svg>
      (555) 014-2290
    </div>
  </nav>
  <h1 class="hero-title" style="left:113px"><span>PERSONALIZED FINANCIAL</span><br>ADVICE TO HELP YOU<br>ACHIEVE YOUR GOALS</h1>
  <h1 class="hero-title" style="left:627px"><span>PROFESSIONAL MANAGEMENT</span><br>TO MAKE YOUR MONEY<br>WORK FOR YOU</h1>
  <svg class="abs" style="left:0;top:0" width="1200" height="850" viewBox="0 0 1200 850">
    <path d="M290 300 v40 q0 10 10 10 h250 q10 0 10 10 v40" fill="none" stroke="#fff" stroke-width="2"/>
    <path d="M0 850 L0 800 Q600 700 1200 835 L1200 850 Z" fill="#fff"/>
    <path d="M80 830 Q600 700 1140 820" fill="none" stroke="#1b7ccc" stroke-width="6"/>
  </svg>
</section>

<section class="who">
  <h2 style="left:138px">WHO WE ARE</h2>
  <p style="left:130px;width:435px">Ravenholt Wealth is an investment advisory firm<br>committed to serving as fiduciary to our clients. We<br>always act in the best interests of our clients, includ-<br>ing putting your interests ahead of our own.</p>
  <div class="divider"></div>
  <h2 style="left:632px">WHO WE SERVE</h2>
  <p style="left:622px;width:436px;font-size:14.5px;line-height:26px">Ravenholt Wealth is for investors looking for the attention<br>and personalization of services typically reserved for ultra<br>high net worth (UHNW) investors. Our founder served<br>UHNW clients at Halvern Bank, Northmark Capital</p>
  <div class="illus" style="left:120px;top:1065px;width:980px;height:300px" role="img" aria-label="Isometric illustration of coin stacks, notepad, banknotes, clock and a falling arrow joined by a blue line"></div>
  <div class="btn" style="left:519px;top:1320px;width:170px;height:46px">LEARN MORE</div>
</section>

<section class="abs why">
  <div class="eyebrow" style="top:58px">WHY WE ARE</div>
  <div class="section-title" style="top:80px">WHY WORK WITH US</div>
  <svg class="abs" style="left:0;top:0" width="1200" height="716">
    <circle cx="495" cy="194" r="5" fill="#fff" stroke="#1b7ccc" stroke-width="2"/>
    <circle cx="725" cy="188" r="5" fill="#fff" stroke="#1b7ccc" stroke-width="2"/>
    <circle cx="467" cy="420" r="5" fill="#fff" stroke="#1b7ccc" stroke-width="2"/>
    <circle cx="762" cy="406" r="5" fill="#fff" stroke="#1b7ccc" stroke-width="2"/>
    <path d="M0 716 L0 700 Q600 590 1200 700 L1200 716 Z" fill="#fff"/>
    <path d="M0 705 Q600 590 1200 705" fill="none" stroke="#1b7ccc" stroke-width="5"/>
  </svg>
  <div class="hub"><div class="hub-img" role="img" aria-label="City skyline photo tinted blue"></div></div>
  <div class="card l" style="left:107px;top:164px"><h3>You Come First</h3><p>We always act in the best interests of our clients</p>
    <div class="icon"><svg width="50" height="50" viewBox="0 0 50 50" fill="none" stroke="#1b7ccc" stroke-width="2"><circle cx="25" cy="18" r="10"/><path d="M25 12v12M28 14h-4a2 2 0 0 0 0 4h2a2 2 0 0 1 0 4h-4"/><path d="M6 38l10-6h8l6 4h10l4-4"/></svg></div></div>
  <div class="card r" style="left:766px;top:160px"><h3>Personalized Services</h3><p>We get to know you in order to service your unique needs</p>
    <div class="icon"><svg width="50" height="50" viewBox="0 0 50 50" fill="none" stroke="#1b7ccc" stroke-width="2"><circle cx="25" cy="20" r="6"/><circle cx="25" cy="20" r="12" stroke-dasharray="4 3"/><path d="M10 40h30"/></svg></div></div>
  <div class="card l" style="left:107px;top:388px"><h3>Transparent Fees</h3><p>You'll always know what you pay and how we get paid</p>
    <div class="icon"><svg width="54" height="44" viewBox="0 0 54 44" fill="none" stroke="#1b7ccc" stroke-width="2"><rect x="6" y="4" width="42" height="28" rx="2"/><path d="M2 38h50"/><text x="27" y="24" text-anchor="middle" font-family="Mulish,sans-serif" font-size="13" fill="#1b7ccc" stroke="none">FEE</text></svg></div></div>
  <div class="card r" style="left:772px;top:384px"><h3>We Give Back</h3><p>We support and better our local communities</p>
    <div class="icon"><svg width="50" height="50" viewBox="0 0 50 50" fill="none" stroke="#1b7ccc" stroke-width="2"><circle cx="28" cy="16" r="9"/><path d="M28 11v10"/><path d="M6 34l8-4h10l4 3h-8M14 40h14l12-8"/></svg></div></div>
  <div class="btn" style="left:526px;top:542px;width:157px;height:44px">VIEW FAQ</div>
</section>

<section class="svc">
  <div class="eyebrow" style="top:2162px">WHAT WE DO</div>
  <div class="section-title" style="top:2182px">OUR SERVICES</div>
  <div class="abs timeline"></div>
  <div class="dot" style="top:2318px"></div>
  <div class="dot" style="top:2654px"></div>
  <div class="dot" style="top:2990px"></div>
  <div class="dot" style="top:3310px"></div>

  <div class="illus" style="left:110px;top:2270px;width:460px;height:265px" role="img" aria-label="Line illustration of financial planning documents, calculator, clock and growth arrows"></div>
  <h3 style="left:616px;top:2314px">FINANCIAL PLANNING</h3>
  <p style="left:616px;top:2356px">Lorem ipsum dolor sit amet, consectetur adipiscing elit, sed do eiusmod tempor incididunt ut labore et dolore magna aliqua. Ut enim ad minim veniam, quis nostrud exercitation ullamco laboris nisi ut aliqu</p>
  <div class="btn" style="left:762px;top:2472px;width:160px;height:44px">LEARN MORE</div>

  <h3 style="left:140px;top:2655px">ASSET MANAGEMENT</h3>
  <p style="left:140px;top:2697px">Lorem ipsum dolor sit amet, consectetur adipiscing elit, sed do eiusmod tempor incididunt ut labore et dolore magna aliqua. Ut enim ad minim veniam, quis nostrud exercitation ullamco laboris nisi ut aliqu</p>
  <div class="btn" style="left:284px;top:2822px;width:160px;height:44px">LEARN MORE</div>
  <div class="illus" style="left:615px;top:2610px;width:450px;height:268px" role="img" aria-label="Line illustration of asset management clipboard with money bag, gears, charts and calendar"></div>

  <div class="illus" style="left:80px;top:2930px;width:480px;height:255px" role="img" aria-label="Line illustration of a laptop with portfolio charts beside a standing advisor"></div>
  <h3 style="left:644px;top:2982px">PORTFOLIO OPTIMIZATION</h3>
  <p style="left:644px;top:3024px">Lorem ipsum dolor sit amet, consectetur adipiscing elit, sed do eiusmod tempor incididunt ut labore et dolore magna aliqua. Ut enim ad minim veniam, quis nostrud exercitation ullamco laboris nisi ut aliqu</p>
  <div class="btn" style="left:777px;top:3144px;width:160px;height:44px">LEARN MORE</div>

  <h3 style="left:120px;top:3290px">ALTERNATIVE INVESTMENTS</h3>
  <p style="left:120px;top:3332px">Lorem ipsum dolor sit amet, consectetur adipiscing elit, sed do eiusmod tempor incididunt ut labore et dolore magna aliqua. Ut enim ad minim veniam, quis nostrud exercitation ullamco laboris nisi ut aliqu</p>
  <div class="btn" style="left:264px;top:3455px;width:160px;height:44px">LEARN MORE</div>
  <div class="illus" style="left:600px;top:3250px;width:496px;height:262px" role="img" aria-label="Line illustration of investment icons around a large outlined word with savings, profit and growth labels"></div>
</section>

<section class="abs contact">
  <div class="label">GET IN TOUCH</div>
  <h2>CONTACT US</h2>
  <div class="info" style="top:216px">
    <svg width="36" height="36" viewBox="0 0 36 36"><circle cx="18" cy="18" r="18" fill="#fff"/><path d="M18 8a7 7 0 0 0-7 7c0 5 7 13 7 13s7-8 7-13a7 7 0 0 0-7-7zm0 9.5a2.5 2.5 0 1 1 0-5 2.5 2.5 0 0 1 0 5z" fill="#1b7ccc"/></svg>
    <div>218 Alder Ridge Rd, Suite #40<br>Fernvale, VA 20000</div>
  </div>
  <div class="info" style="top:288px">
    <svg width="36" height="36" viewBox="0 0 36 36"><circle cx="18" cy="18" r="18" fill="#fff"/><path transform="translate(8 8) scale(.85)" fill="#1b7ccc" d="M6.6 10.8a15 15 0 0 0 6.6 6.6l2.2-2.2c.3-.3.7-.4 1-.2 1.1.4 2.3.6 3.6.6.6 0 1 .4 1 1V20c0 .6-.4 1-1 1A17 17 0 0 1 3 4c0-.6.4-1 1-1h3.5c.6 0 1 .4 1 1 0 1.3.2 2.5.6 3.6.1.3 0 .7-.2 1z"/></svg>
    <div>(555) 014-2290</div>
  </div>
  <div class="abs" style="left:110px;top:340px;width:410px;height:180px;background:radial-gradient(ellipse 50% 55% at 55% 55%,#1a3a5e 0%,#2a5f93 40%,rgba(120,180,230,.55) 65%,rgba(27,124,204,0) 100%)" role="img" aria-label="Illustrated mountain silhouette with a location marker"></div>
  <div class="form">
    <div class="field" style="left:32px;top:55px;width:238px">First Name</div>
    <div class="field" style="left:278px;top:55px;width:238px">Last Name</div>
    <div class="field" style="left:32px;top:109px;width:238px">Email address</div>
    <div class="field" style="left:278px;top:109px;width:238px">Phone</div>
    <div class="field" style="left:32px;top:163px;width:484px;height:108px;border-radius:14px">Message</div>
    <div class="send">SEND MESSAGE</div>
  </div>
  <svg class="abs" style="left:0;top:470px" width="1200" height="90"><path d="M0 90 L0 60 Q600 -30 1200 60 L1200 90 Z" fill="#050608"/></svg>
</section>

<footer class="abs footer">
  <div class="col" style="left:142px;top:134px">
    <div style="display:flex;align-items:center;gap:10px;font-size:21px;font-weight:500;letter-spacing:1px">
      <span style="width:30px;height:30px;border:2px solid #fff;display:inline-block"></span>RAVENHOLT WEALTH
    </div>
    <p style="margin-top:26px;width:290px;font-size:12.5px;line-height:16px;color:#b8bec5">Lorem ipsum dolor sit amet, consectetur adipiscing elit, sed do eiusmod tempor incididunt ut labore et dolore</p>
  </div>
  <div class="vbar" style="left:482px"></div>
  <div class="col" style="left:505px"><h4>NAVIGATION</h4><ul><li>Home</li><li>About Us</li><li>Services</li><li>FAQ</li><li>Contact Us</li></ul></div>
  <div class="vbar" style="left:690px"></div>
  <div class="col" style="left:713px"><h4>CONTACT US</h4>
    <div style="display:flex;gap:12px;font-size:13.5px;line-height:19px"><svg width="26" height="26" viewBox="0 0 36 36"><circle cx="18" cy="18" r="18" fill="#fff"/><path d="M18 8a7 7 0 0 0-7 7c0 5 7 13 7 13s7-8 7-13a7 7 0 0 0-7-7zm0 9.5a2.5 2.5 0 1 1 0-5 2.5 2.5 0 0 1 0 5z" fill="#050608"/></svg><div>218 Alder Ridge Rd, Suite #40<br>Fernvale, VA 20000</div></div>
    <div style="display:flex;gap:12px;font-size:13.5px;margin-top:22px;align-items:center"><svg width="26" height="26" viewBox="0 0 36 36"><circle cx="18" cy="18" r="18" fill="#fff"/><path transform="translate(8 8) scale(.85)" fill="#050608" d="M6.6 10.8a15 15 0 0 0 6.6 6.6l2.2-2.2c.3-.3.7-.4 1-.2 1.1.4 2.3.6 3.6.6.6 0 1 .4 1 1V20c0 .6-.4 1-1 1A17 17 0 0 1 3 4c0-.6.4-1 1-1h3.5c.6 0 1 .4 1 1 0 1.3.2 2.5.6 3.6.1.3 0 .7-.2 1z"/></svg>(555) 014-2290</div>
  </div>
  <div class="vbar" style="left:954px"></div>
  <div class="col" style="left:977px"><h4>FOLLOW US</h4><span style="display:block;width:32px;height:32px;border-radius:50%;background:#fff"></span></div>
  <div class="foot-rule"></div>
  <div class="copyright">© 2022 Ravenholt Wealth All Rights Reserved</div>
</footer>

</body>
</html>
```